New Plumbing Company

We are looking for a smart and creative business card design for our new plumbing company. We are looking for creativity and originality in our business cards.

Industry/Entity Type

Plumbing

Contact Information for Business Card

Kelvora Plumbing
Peter Oswalt
Managing Director
Telephone Number : 0481529046
Email : service@kelvoraplumbing.com.au
Website : www.kelvoraplumbing.com.au
Lic. 318462D

Colors
0692cd
33a6d7
000000

Requirements
Must have
• I want the business card to be designed on a black background using the blue tones i have selected as seen in the company logo.

```html
<!DOCTYPE html>
<html lang="en">
<head>
<meta charset="UTF-8">
<title>Kelvora Plumbing — Business Card</title>
<link rel="stylesheet" href="https://fonts.googleapis.com/css2?family=Jost:wght@400;500&display=swap">
<style>
  :root {
    --blue: #0692cd;
    --blue-light: #33a6d7;
    --black: #000000;
    --card-black: #0a0a0a;
    --white: #ffffff;
    --stage: #e9ebee;
  }
  * { margin: 0; padding: 0; box-sizing: border-box; }
  html, body { width: 1200px; height: 843px; overflow: hidden; }
  body {
    background: var(--stage);
    font-family: "Jost", "Futura", sans-serif;
    display: flex;
    align-items: center;
    justify-content: center;
    gap: 40px;
  }
  .card {
    position: relative;
    width: 540px;
    height: 309px;
    overflow: hidden;
    box-shadow: 0 10px 28px rgba(0,0,0,0.25);
  }

  /* Back side */
  .card--back {
    background: var(--blue);
    color: var(--black);
  }
  .back-mark {
    position: absolute;
    top: 92px;
    left: 0;
    right: 0;
    display: flex;
    align-items: center;
    justify-content: center;
    gap: 12px;
  }
  .back-mark .dot {
    width: 22px; height: 22px;
    border: 3px solid var(--black);
    border-radius: 50%;
  }
  .back-mark .name {
    font-size: 30px;
    font-weight: 500;
    letter-spacing: 0.5px;
  }
  .back-web {
    position: absolute;
    top: 212px;
    left: 0; right: 0;
    text-align: center;
    font-size: 14px;
    letter-spacing: 0.6px;
  }

  /* Front side */
  .card--front {
    background: var(--card-black);
    color: var(--white);
  }
  .band {
    position: absolute;
    inset: 0;
    width: 540px;
    height: 309px;
  }
  .person {
    position: absolute;
    top: 30px;
    left: 40px;
  }
  .person .name {
    font-size: 19px;
    font-weight: 500;
    letter-spacing: 0.8px;
    text-transform: uppercase;
  }
  .person .role {
    font-size: 14px;
    margin-top: 2px;
    letter-spacing: 0.3px;
  }
  .brand {
    position: absolute;
    top: 118px;
    right: 26px;
    display: flex;
    align-items: center;
    gap: 10px;
  }
  .brand .dot {
    width: 34px; height: 34px;
    border: 3px solid var(--blue-light);
    border-radius: 50%;
  }
  .brand .name {
    font-size: 27px;
    font-weight: 500;
    color: var(--blue-light);
  }
  .contact {
    position: absolute;
    top: 136px;
    left: 40px;
    list-style: none;
    font-size: 13px;
    line-height: 19px;
    letter-spacing: 0.3px;
  }
  .licence {
    position: absolute;
    right: 30px;
    bottom: 26px;
    font-size: 15px;
    letter-spacing: 0.6px;
  }
</style>
</head>
<body>

  <section class="card card--back" aria-label="Business card back">
    <div class="back-mark">
      <span class="dot"></span>
      <span class="name">Kelvora Plumbing</span>
    </div>
    <p class="back-web">www.kelvoraplumbing.com.au</p>
  </section>

  <section class="card card--front" aria-label="Business card front">
    <svg class="band" viewBox="0 0 540 309" aria-hidden="true">
      <polygon points="0,20 300,20 360,95 0,95" fill="var(--blue)"/>
    </svg>
    <div class="person">
      <p class="name">Peter Oswalt</p>
      <p class="role">Managing Director</p>
    </div>
    <div class="brand">
      <span class="dot"></span>
      <span class="name">Kelvora Plumbing</span>
    </div>
    <ul class="contact">
      <li>0481529046</li>
      <li>service@kelvoraplumbing.com.au</li>
      <li>www.kelvoraplumbing.com.au</li>
    </ul>
    <p class="licence">Lic. 318462D</p>
  </section>

</body>
</html>
```